Ridgeline Throttle Touring Company needs brochure

We need a brochure for our motorcycle tour company, we run tours and provide other services like day rides, bespoke trips, heli taxis, trekking, mountain biking, white water rafting etc. We are a small company that runs the tours ourselves, providing excellent customer service . We are team of international friendly motorcycle enthusiasts with a passion for Nepal. With an office in the UK and in Nepal. Our brochure should reflect quality adventures, showcasing the Nepal Himalayas, our tours, and shout adventure. Target audience are Adventure Bikers. Below are some photos (all of which are owned by us, for use on our brochure only) Also the document with all the content for the brochure.

Target Market(s)

Adventure Motorbike Riders

Industry/Entity Type

Travel

Other font styles liked:
• Aurora for headings...

Requirements
Must have
• Adventure Feel. Looking cool and modern. Well thought out colour palette. Include big photos. Sometimes as background to text.
• touring in the himalayas:
Nice to have
• Infographics for the include exclude section.
• Want it to be A5 brochure, landscape, probably be needing 14 pages. Might make it shorter to 12 if possible.
• If you have access to vectors/graphics please use stuff related to Nepal like Buddhas eyes, stupas, prayer flags, bells, shiva trident, mountains, tyre tracks etc. Be imaginative and creative. I have uploaded a photo of rough layout but is quite open to interpretation. Need photos and text to be clear. Please let me know if any photos are not good quality.
Should not have
• It shouldn't look like a corporate brochure, boring,
• It shouldn't look like a Brokker Vantell type trip. We use adventure bikes.

```html
<!DOCTYPE html>
<html lang="en">
<head>
<meta charset="utf-8">
<title>Ridgeline Throttle Touring Company – Brochure</title>
<link rel="stylesheet" href="https://fonts.googleapis.com/css2?family=Michroma&family=Questrial&display=swap">
<style>
  :root{
    --backdrop:#b5dbdb;
    --paper:#f4f4f2;
    --red:#d42a2a;
    --red-deep:#b31218;
    --navy:#1e2c55;
    --sky:#4a66ab;
    --ink:#3a3a3a;
    --white:#ffffff;
  }
  *{box-sizing:border-box;margin:0;padding:0}
  html,body{width:711px;height:1200px;overflow:hidden}
  body{background:var(--backdrop);font-family:"Questrial",sans-serif;color:var(--ink);position:relative}

  /* ---------- front cover ---------- */
  .cover{position:absolute;width:520px;height:368px;overflow:hidden;box-shadow:0 10px 24px rgba(0,0,0,.18)}
  .cover--hero{left:96px;top:56px}
  .cover__photo{position:absolute;inset:0;
    background:linear-gradient(100deg,#1b2750 0%,#24325c 30%,#4f5f86 46%,#8d8a8a 60%,#b4402f 72%,#8e7a62 86%,#6f5f4c 100%)}
  .cover__shade{position:absolute;left:0;top:0;bottom:0;width:48%;background:linear-gradient(90deg,rgba(18,26,56,.55),rgba(18,26,56,0))}
  .cover__brand{position:absolute;left:40px;top:58px;display:flex;align-items:center;gap:10px}
  .cover__brand-dot{width:22px;height:22px;border-radius:50%;background:var(--red)}
  .cover__brand-name{font-family:"Questrial",sans-serif;color:var(--white);font-size:15px;line-height:1.2;width:150px}
  .cover__title{position:absolute;left:40px;top:180px;font-family:"Michroma",sans-serif;font-weight:400;color:var(--white);line-height:1.02}
  .cover__title span{display:block}
  .cover__title .t1{font-size:19px}
  .cover__title .t2{font-size:29px}
  .cover__url{position:absolute;left:40px;bottom:26px;color:var(--white);font-size:12px;letter-spacing:1.5px}

  /* ---------- spreads ---------- */
  .spread{position:absolute;left:26px;width:660px;height:234px;display:flex;box-shadow:0 10px 22px rgba(0,0,0,.18)}
  .spread--outer{top:500px}
  .spread--inner{top:840px}
  .page{position:relative;width:330px;height:234px;overflow:hidden;background:var(--paper)}
  /* pages are laid out at double size, then scaled to fit */
  .page__art{position:absolute;left:0;top:0;width:660px;height:468px;transform:scale(.5);transform-origin:0 0}
  .page--left .page__art::after,.page--right .page__art::after{content:"";position:absolute;top:0;bottom:0;width:18px;pointer-events:none}
  .page--left .page__art::after{right:0;background:linear-gradient(90deg,rgba(0,0,0,0),rgba(0,0,0,.18))}
  .page--right .page__art::after{left:0;background:linear-gradient(270deg,rgba(0,0,0,0),rgba(0,0,0,.18))}

  .cover--mini{left:0;top:0;transform:scale(1.2692);transform-origin:0 0;box-shadow:none}

  /* back cover */
  .back__panel{position:absolute;left:0;top:0;bottom:0;width:372px;background:linear-gradient(120deg,var(--red) 0%,var(--red-deep) 100%);color:var(--white);padding:38px 20px 16px 24px;font-size:8.6px;line-height:1.35}
  .back__sky{position:absolute;left:372px;right:0;top:0;height:120px;background:var(--sky)}
  .back__map{position:absolute;left:396px;top:28px;width:236px;height:168px;background:linear-gradient(135deg,#d8d8d8,#8d8d8d);border:2px solid #333}
  .back__landscape{position:absolute;left:372px;right:0;top:120px;bottom:0;background:linear-gradient(180deg,#7b7d86 0%,#b19b7c 35%,#8b7a49 60%,#c9b48f 100%)}
  .back__h{font-family:"Michroma",sans-serif;font-weight:400;font-size:10px;line-height:1.25;margin:8px 0 3px}
  .back__strong{font-weight:bold;font-size:8.6px;margin-top:5px}
  .contact-row{display:flex;gap:8px;align-items:center;margin-top:2px}
  .contact-row svg{width:9px;height:9px;flex:none}

  /* inner spread */
  .photo{position:absolute}
  .photo--sunset{left:36px;top:44px;width:400px;height:196px;background:linear-gradient(180deg,#6b6e78 0%,#e0a04a 30%,#a25a2c 55%,#2b4a64 80%,#1e3146 100%)}
  .photo--village{left:444px;top:160px;width:216px;height:124px;background:linear-gradient(160deg,#9fb0a3,#5c6e45 60%,#8a6d55)}
  .photo--cyclists{left:444px;top:292px;width:216px;height:140px;background:linear-gradient(180deg,#3c5fa6,#7a97c9 60%,#33384a)}
  .about{position:absolute;left:36px;top:250px;width:396px;font-size:8.6px;line-height:1.3}
  .section-title{font-family:"Michroma",sans-serif;font-weight:400;color:var(--red);font-size:14px;line-height:1.2;margin-bottom:5px}
  .about p{margin-bottom:5px}

  .social{position:absolute;left:28px;top:30px;width:612px;font-size:8.2px;line-height:1.32}
  .bio{position:absolute;font-size:8px;line-height:1.32}
  .bio b{font-size:8.6px}
  .photo--arjun{left:28px;top:116px;width:190px;height:96px;background:linear-gradient(160deg,#4e7a3c,#8aa46a 55%,#6b6a5e)}
  .bio--arjun{left:236px;top:112px;width:404px}
  .photo--lake{left:444px;top:196px;width:196px;height:92px;background:linear-gradient(180deg,#8c95a2,#c9cbd0 45%,#2c3340)}
  .bio--maya{left:28px;top:226px;width:396px}
  .photo--bridge{left:56px;top:340px;width:220px;height:108px;background:linear-gradient(150deg,#5d7a44,#a6ab9e 55%,#6c7766)}
  .bio--kenji{left:316px;top:304px;width:324px}
</style>
</head>
<body>

  <!-- Front cover -->
  <section class="cover cover--hero" aria-label="Front cover">
    <div class="cover__photo" role="img" aria-label="Photo of an adventure rider in a helmet with a red dirt bike on a high Himalayan desert road under blue sky"></div>
    <div class="cover__shade"></div>
    <div class="cover__brand">
      <span class="cover__brand-dot"></span>
      <span class="cover__brand-name">Ridgeline Throttle Touring Company</span>
    </div>
    <h1 class="cover__title"><span class="t1">THE ULTIMATE</span><span class="t2">HIMALAYAN</span><span class="t2">MOTORCYCLE</span><span class="t2">ADVENTURE</span></h1>
    <div class="cover__url">www.ridgelinethrottle.co.uk</div>
  </section>

  <!-- Back + front cover spread -->
  <section class="spread spread--outer" aria-label="Back and front cover">
    <div class="page page--left">
      <div class="page__art">
        <div class="back__sky"></div>
        <div class="back__landscape" role="img" aria-label="Photo of a rider crossing a dry valley with autumn trees and mountains"></div>
        <div class="back__map" role="img" aria-label="Grey map showing the route from Europe to Nepal"></div>
        <div class="back__panel">
          <h2 class="back__h">WHERE TO FIND US?</h2>
          <p>With one foot in the UK and one foot in Nepal, we are ideally placed to organise your Himalayan adventures.</p>
          <h2 class="back__h">GOT A DREAM OF TRAVELLING TO THE HIMALAYAS?</h2>
          <p>I'll be your first contact right here in the UK to answer any questions regarding travelling to Nepal or Tibet. Don't hesitate to reach me via email or directly on my mobile.</p>
          <p class="back__strong">LOOKING FORWARD TO HEARING FROM YOU!</p>
          <p class="back__strong">Maya</p>
          <div class="contact-row">Mobile/ Whats app:
            <svg viewBox="0 0 10 10"><path d="M2 1l2 2-1 1.2c.6 1.3 1.5 2.2 2.8 2.8L7 6l2 2-1.3 1.3C4.5 9 1 5.5.7 2.3z" fill="#fff"/></svg>(+44)07700 900412</div>
          <div class="contact-row" style="padding-left:88px">
            <svg viewBox="0 0 10 10"><rect x="1" y="2" width="8" height="6" fill="none" stroke="#fff"/><path d="M1 2l4 3.5L9 2" fill="none" stroke="#fff"/></svg>maya@ridgelinethrottle.co.uk</div>
          <h2 class="back__h">ALREADY IN KATHMANDU?</h2>
          <p>Come visit us at our office in Kanti Path, Kathmandu. You can rent one of our bikes for your own self guided tour or book a guided day ride if you want to experience the Himalayas by motorcycle but don't have much time.</p>
          <p style="margin-top:3px"><b>Kenji</b> or <b>Arjun</b> will be there to assist you.</p>
          <div class="contact-row">Mobile: <svg viewBox="0 0 10 10"><path d="M2 1l2 2-1 1.2c.6 1.3 1.5 2.2 2.8 2.8L7 6l2 2-1.3 1.3C4.5 9 1 5.5.7 2.3z" fill="#fff"/></svg>(+977)9800 000123</div>
          <div class="contact-row">Office: <svg viewBox="0 0 10 10"><path d="M2 1l2 2-1 1.2c.6 1.3 1.5 2.2 2.8 2.8L7 6l2 2-1.3 1.3C4.5 9 1 5.5.7 2.3z" fill="#fff"/></svg>(+977)01 4000 500</div>
          <p style="margin-top:6px">Check out our website for more details or find us on our social pages (@ridgeline.throttle), like, follow and subscribe for all our news and updates.</p>
        </div>
      </div>
    </div>
    <div class="page page--right">
      <div class="page__art">
        <div class="cover cover--mini">
          <div class="cover__photo" role="img" aria-label="Photo of an adventure rider with a red dirt bike on a Himalayan road"></div>
          <div class="cover__shade"></div>
          <div class="cover__brand">
            <span class="cover__brand-dot"></span>
            <span class="cover__brand-name">Ridgeline Throttle Touring Company</span>
          </div>
          <div class="cover__title"><span class="t1">THE ULTIMATE</span><span class="t2">HIMALAYAN</span><span class="t2">MOTORCYCLE</span><span class="t2">ADVENTURE</span></div>
          <div class="cover__url">www.ridgelinethrottle.co.uk</div>
        </div>
      </div>
    </div>
  </section>

  <!-- Inner spread -->
  <section class="spread spread--inner" aria-label="Inner pages">
    <div class="page page--left">
      <div class="page__art">
        <div class="photo photo--sunset" role="img" aria-label="Photo of wooden boats on a lake at sunset with hazy hills"></div>
        <div class="photo photo--village" role="img" aria-label="Photo of riders above a hillside village"></div>
        <div class="photo photo--cyclists" role="img" aria-label="Photo of mountain bikers silhouetted against a blue sky"></div>
        <div class="about">
          <h2 class="section-title">ABOUT US</h2>
          <p>Here at Ridgeline Throttle we are the creators and the providers of all our motorcycle tours.</p>
          <p>With a life-time of experience behind us with riding the roads in the Himalayas our unique motorcycle trips will show you the world's tallest peaks, take you over the other side of the Himalayas into Tibet, explore the tropical southern flatlands, home of the Royal Bengal Tiger and bring you to the birthplace of Buddha.</p>
          <p>We have a fleet of Tarrow TR250, these bikes are light and agile, with a good handful of torque when you need it, perfectly suited to the mountainous terrain. And they are all fitted with ABS plus a digital dash.</p>
          <p>Anyone is welcome to sign up to one of our Himalayan motorcycle adventures, no matter what gender, age, ethnicity or belief.</p>
        </div>
      </div>
    </div>
    <div class="page page--right">
      <div class="page__art">
        <div class="social">
          <h2 class="section-title">SOCIAL WORK</h2>
          <p>Each trip we run helps provide funds for our social projects in Nepal. We currently give to the Himal Bright Science Scholarship Fund, which provides outstanding students from Sindhuli District with tuition and maintenance fees for university in Nepal. Sindhuli District is close to our hearts and we would like to see this part of Nepal develop and flourish. The scholarship fund is one of the best ways to give young students a chance for further education.</p>
        </div>
        <div class="photo photo--arjun" role="img" aria-label="Photo of a rider on a motorbike on a green mountain track"></div>
        <div class="bio bio--arjun"><b>Arjun</b> With many journeys both on motorbike and on foot with his friends, colleagues and clients across Nepal, travel and adventure are in his blood. Arjun's military background makes it possible to provide personal welcomes across the country and handle any problem met on the challenging terrain. He is a huge asset to the team and puts his heart and soul into everything he does, so you can rely on him to make your adventure the most epic it could be.</div>
        <div class="photo photo--lake" role="img" aria-label="Photo of a traveller overlooking a calm lake"></div>
        <div class="bio bio--maya"><b>Maya</b> will travel with you to make sure your experience is unforgettable. Coming from a background in Public Health, Maya has lived in Peru, Spain, the Netherlands and Nepal. She is from the UK and was educated at university abroad. As well as working to make your trip to Nepal a great experience, she is your first contact in the UK for help with flight tickets, visas, vaccinations (or simply what to pack!) via phone or email.</div>
        <div class="photo photo--bridge" role="img" aria-label="Photo of a rider crossing a suspension bridge"></div>
        <div class="bio bio--kenji"><b>Kenji</b> With 30 years of work in the tourism industry he brings a lot of experience to the team. Having a keen sense for detail his mechanical abilities often save the day, and when not on a motorbike he's driving the support vehicle like a pro. Always friendly and easy-going he's great company and has a depth of technical knowledge about Nepal ranging from its architecture to its helicopters!</div>
      </div>
    </div>
  </section>

</body>
</html>
```